International freight forwarder experienced in perishable handling needs a web design

We need a website designed that will allow us to capture more customers through the website. We would like a visually appealing design that is not so heavy on text. Our business covers the logistics and freight forwarding industries and we have offices in South America and the USA. Our main customers are importers USA, Europe, Asia and Russia and we currently work almost exclusively with perishable products such as fresh cut flowers, fresh exotics fruits, cacao, fresh fish etc. We would like to convey a fresh, modern approach to freight forwarding focusing on concepts such as - time sensitive, anytime-anywhere delivery, innovation, experience, reliability and confidence. Should include links with Plumetta and Worvanet. Our core solutions include: Core Services
*Air Freight
*Ocean Freight
*Warehousing & Distribution
Our industry solutions cover
*Flowers
*FMCG including, fruits, vegetables
*Live animals
*Automotive
*Consumer Goods
*Industrial
*Oil & Gas
*Pharma
* Event logistics
* Project logistics

Target Market(s)

Importers in Europe, USA, Asia, Middle East and Russia

Number of Pages Required

4 page

Font styles to use
Sans Serif

Colors
a1cd39
606060
000000

Requirements
Must have
• Photos of fresh cut flowers, FMCG such as cacao, fresh fish (packaged for shipping), fresh exotic fruits, pharma products (packaged for shipping), oil and gas etc. Internal customer login access
Nice to have
• Photos of cargo shipping carriers and cargo airline carriers. Features similar to those of following website http://www.brolvacargo.com/eng/main/index.jsp?FromURL=web
Should not have
• Too much text, needs to be visually pleasing

```html
<!DOCTYPE html>
<html lang="en">
<head>
<meta charset="utf-8">
<title>Veltrano Alliance Group</title>
<link rel="stylesheet" href="https://fonts.googleapis.com/css2?family=Open+Sans:wght@400;600;700&display=swap">
<style>
:root{
  --green:#8fbe28;
  --text:#606060;
  --heading:#555557;
  --card:#d9d9d9;
  --footer:#4a4a4c;
  --btn:#4d4d4f;
  --white:#ffffff;
  --sky-deep:#0a4a96;
  --sky-mid:#2f8fe0;
  --sky-light:#cdeafd;
}
*{margin:0;padding:0;box-sizing:border-box}
html,body{width:874px;height:1200px;overflow:hidden;background:var(--white)}
body{position:relative;font-family:'Open Sans',sans-serif;color:var(--text)}
.abs{position:absolute}
.brand{left:78px;top:16px;display:flex;align-items:center;gap:8px}
.brand-mark{width:30px;height:30px;border-radius:50%;background:var(--green)}
.brand-name{font-size:22px;font-weight:600;color:var(--heading);letter-spacing:-.5px;line-height:1}
.brand-sub{left:198px;top:52px;font-size:6.5px;letter-spacing:3px;color:#999}
.tagline{right:72px;top:30px;font-family:Arial,sans-serif;font-size:8px;color:#555}
.main-nav{right:72px;top:51px;display:flex;gap:18px;font-size:10.5px;font-weight:700;color:#333}
.main-nav .active{color:var(--green)}
.hero{left:0;top:76px;width:874px;height:427px;
  background:
    radial-gradient(circle at 42% 58%,rgba(235,248,255,.85) 0%,rgba(190,228,252,.55) 14%,rgba(120,190,242,0) 34%),
    radial-gradient(circle at 80% 30%,rgba(210,238,255,.6) 0%,rgba(150,210,250,0) 22%),
    radial-gradient(circle at 58% 105%,#8fcaf6 0%,#4aa2ea 38%,#1d72c8 60%,rgba(10,74,150,0) 61.5%),
    radial-gradient(ellipse at 50% 110%,#3c8fdc 0%,#1a63b6 55%,var(--sky-deep) 85%)}
.services{left:94px;top:410px;width:687px;height:270px;background:var(--white)}
.card{top:419px;width:163px;height:255px;background:var(--card)}
.card-top{height:84px;background:var(--green);text-align:center;color:var(--white);font-weight:700;font-size:10.5px;padding-top:15px}
.card-photo{position:absolute;left:41px;top:38px;width:80px;height:80px;border-radius:50%;border:3px solid #eee}
.card p{position:absolute;left:15px;top:130px;width:142px;font-size:9.2px;line-height:11.4px;color:#555}
.read-more{position:absolute;left:15px;top:223px;width:56px;height:16px;background:var(--btn);color:var(--white);font-size:6.5px;display:flex;align-items:center;gap:5px;padding-left:5px}
.section-title{font-size:22px;font-weight:700;color:var(--heading);line-height:1}
.welcome-text{left:105px;top:749px;width:350px;font-size:9.4px;line-height:11.3px;color:#555}
.device-visual{left:86px;top:830px;width:199px;height:154px;background:linear-gradient(135deg,#d4d4d4,#7b7b7b 60%,#2c2c2c);border-radius:6px}
.track-note{left:297px;top:828px;font-family:Arial,sans-serif;font-size:10px;line-height:12.5px;color:#333}
.track-field{left:298px;top:866px;width:149px;height:70px;background:#ececec;border:1px solid #c8c8c8;border-radius:3px}
.track-btn{left:302px;top:950px;width:58px;height:21px;background:var(--btn);color:var(--white);font-size:8.5px;font-weight:600;border-radius:2px;display:flex;align-items:center;justify-content:center}
.news{left:526px;width:244px}
.news-date{position:absolute;left:0;top:0;width:24px;height:24px;border-radius:50%;background:var(--green);color:var(--white);font-size:9px;font-weight:700;display:flex;align-items:center;justify-content:center}
.news-month{position:absolute;left:1px;top:26px;font-size:9.5px;font-weight:700;color:#555}
.news-title{position:absolute;left:44px;top:-6px;width:190px;font-size:10px;font-weight:700;color:var(--green);line-height:12.5px}
.news-body{position:absolute;left:45px;top:22px;width:192px;font-family:Arial,sans-serif;font-size:9.2px;line-height:11.4px;color:#444}
.news-rule{left:526px;top:854px;width:244px;height:1px;background:#ccc}
.footer{left:0;top:1027px;width:874px;height:173px;background:var(--footer);color:var(--white)}
.footer h3{position:absolute;top:38px;font-size:18px;font-weight:600}
.foot-links{position:absolute;top:74px;font-family:Arial,sans-serif;font-size:10.4px;line-height:12.2px;list-style:none}
.social{position:absolute;top:76px;width:32px;height:32px;border-radius:50%;background:var(--white)}
.contact-lines{position:absolute;left:444px;top:74px;font-family:Arial,sans-serif;font-size:10.4px;line-height:12.5px}
.phone{position:absolute;left:440px;top:104px;display:flex;align-items:center;gap:5px;font-size:16px;font-weight:600}
.foot-brand{position:absolute;left:616px;top:40px;display:flex;align-items:center;gap:7px}
.foot-brand .brand-mark{background:#8a8a8a;width:26px;height:26px}
.foot-brand span{font-size:19px;font-weight:600;color:var(--white)}
.copyright{position:absolute;left:621px;top:82px;font-family:Arial,sans-serif;font-size:7.2px;line-height:9.5px}
</style>
</head>
<body>
<header>
  <div class="abs brand"><span class="brand-mark"></span><span class="brand-name">Veltrano Alliance</span></div>
  <div class="abs brand-sub">GROUP</div>
  <div class="abs tagline">Expert Importers in Europe, USA, Asia, Middle East and Russia</div>
  <nav class="abs main-nav"><span class="active">HOME</span><span>ABOUT US</span><span>SERVICES</span><span>TECHNOLOGY</span><span>CONTACT US</span></nav>
</header>

<div class="abs hero" role="img" aria-label="Glowing blue globe with light trails of shipping routes linking Europe, Africa and Asia"></div>

<section>
  <div class="abs services"></div>
  <div class="abs card" style="left:105px">
    <div class="card-top">TRANSPORTATION</div>
    <div class="card-photo" role="img" aria-label="Container ship at sea" style="background:linear-gradient(#7db4dc,#3c5f7c 60%,#1e2b36)"></div>
    <p>Lorem ipsum dolor sAit amet, consectetur adipisicEing elit, eiusmod tempor incidiDdunt ut labore et dolore maBgna aliqua. enim ad minim veniam, quis nostrud exercitatBion ullamco laboris nisi ut aliqBuip ex ea co.</p>
    <div class="read-more"><svg width="9" height="8" viewBox="0 0 9 8"><path d="M0 4h7M4 1l3 3-3 3" stroke="#fff" stroke-width="1.3" fill="none"/></svg>read more</div>
  </div>
  <div class="abs card" style="left:273px">
    <div class="card-top">FREIGHT MANAGEMENT</div>
    <div class="card-photo" role="img" aria-label="Container port with cranes at dusk" style="background:linear-gradient(#6f8fc4,#a56a3c 60%,#3a2d36)"></div>
    <p>Duis aute irure dolor in rephen derit in volupttte velit essecillum dolore eu fugiat nulla pariatur. Excepter sint occaecat upidatat non proident, sunt in culpa qui officia deserunt mollniSS id est laborum.</p>
    <div class="read-more"><svg width="9" height="8" viewBox="0 0 9 8"><path d="M0 4h7M4 1l3 3-3 3" stroke="#fff" stroke-width="1.3" fill="none"/></svg>read more</div>
  </div>
  <div class="abs card" style="left:440px">
    <div class="card-top">WAREHOUSING</div>
    <div class="card-photo" role="img" aria-label="Forklift in a warehouse" style="background:linear-gradient(#8a5a3a,#d46b2a 55%,#3c2a22)"></div>
    <p>Sed ut perspiciatis, unde omnis iste natus error sit volptatem accusantium doloreme laudan tium, totam rem aperiam eaque ipsa, quae ab illo intore veritati et quasi architecto beatae vitae dicta sunt.</p>
    <div class="read-more"><svg width="9" height="8" viewBox="0 0 9 8"><path d="M0 4h7M4 1l3 3-3 3" stroke="#fff" stroke-width="1.3" fill="none"/></svg>read more</div>
  </div>
  <div class="abs card" style="left:608px">
    <div class="card-top">TECHNOLOGY</div>
    <div class="card-photo" role="img" aria-label="Touch screen display" style="background:linear-gradient(#c9ccd1,#3a3d42 55%,#9a9da3)"></div>
    <p>At vero eo et acusamus et iusto odio dignissimos ducimus, qui blanditiis praentium voluptatum deleniti atque corrupti, quos dolores et quas motias excepturi sint, obcaecati cupiditate non provident, similique.</p>
    <div class="read-more"><svg width="9" height="8" viewBox="0 0 9 8"><path d="M0 4h7M4 1l3 3-3 3" stroke="#fff" stroke-width="1.3" fill="none"/></svg>read more</div>
  </div>
</section>

<section>
  <h2 class="abs section-title" style="left:103px;top:714px">WELCOME TO VELTRANOALLIANCE</h2>
  <p class="abs welcome-text">We currently work almost exclusively with perishable products such as fresh cut flowers, fresh exotics fruits, cacao, fresh fish etc. We convey a fresh, modern approach to freight forwarding focusing on concepts such as - time sensitive, anytime-anywhere delivery, innovation, experience, reliability and confidence.</p>
  <div class="abs device-visual" role="img" aria-label="Monitor and tablet showing a world map and warehouse tracking"></div>
  <p class="abs track-note">Track up to 10 numbers at a time.<br>Separate with return</p>
  <div class="abs track-field"></div>
  <div class="abs track-btn">TRACK</div>
</section>

<section>
  <h2 class="abs section-title" style="left:528px;top:714px">LATEST NEWS</h2>
  <article class="abs news" style="top:754px">
    <div class="news-date">23</div><div class="news-month">AUG</div>
    <div class="news-title">UNDE OMNIS ISTE NATUS ERROR SIT VOLUPTATEM</div>
    <p class="news-body">Aspernatur aut odit aut fugit, sed quia consequuntur magni dolores eos, qui ratione voluptatem sequi nesciunt, neque porro quisquam est, qui dolorem ipsum, quia dolor sit amet consectetur.</p>
  </article>
  <div class="abs news-rule"></div>
  <article class="abs news" style="top:877px">
    <div class="news-date">23</div><div class="news-month">AUG</div>
    <div class="news-title">UNDE OMNIS ISTE NATUS ERROR SIT VOLUPTATEM</div>
    <p class="news-body">Aspernatur aut odit aut fugit, sed quia consequuntur magni dolores eos, qui ratione voluptatem sequi nesciunt, neque porro quisquam est, qui dolorem ipsum, quia dolor sit amet consectetur.</p>
  </article>
</section>

<footer class="abs footer">
  <h3 style="left:79px">NAVIGATION</h3>
  <ul class="foot-links" style="left:78px"><li>Home</li><li>About us</li><li>Services</li><li>Technology</li></ul>
  <ul class="foot-links" style="left:156px"><li>Contact Us</li><li>Sitemap</li><li>Privacy Policy</li><li>Terms</li></ul>
  <h3 style="left:266px">CONNECT</h3>
  <span class="social" style="left:266px" aria-label="Social link"></span>
  <span class="social" style="left:307px" aria-label="Plumetta"></span>
  <span class="social" style="left:349px" aria-label="Worvanet"></span>
  <h3 style="left:443px">CONTACT US</h3>
  <div class="contact-lines">#38 street city, state, Country<br>info@veltranoalliance.com</div>
  <div class="phone"><svg width="18" height="18" viewBox="0 0 18 18"><circle cx="9" cy="9" r="8" stroke="#fff" stroke-width="1.2" fill="none"/><path d="M6 4.5l2 2-1 1.3c.6 1.4 1.6 2.4 3 3l1.2-1 2 2-1.3 1.5C9.5 13 5 8.5 4.7 6z" fill="#fff"/></svg>014.555.0182</div>
  <div class="foot-brand"><span class="brand-mark"></span><span>Veltrano Alliance</span></div>
  <div class="copyright">© Veltrano Alliance<br>All Rights Reserved 2013</div>
</footer>
</body>
</html>
```